Ice Cream Cup Design

We need a packaging design for ice cream cups.
We're a London based company called Villa Rosa Dolci and are producers of fresh Italian Artisan Gelato our website is www.villarosadolci.co.uk

We're looking to invest in a cup filling machine to fill 100ml and 500ml cups of gelato.
The 500ml cup will be the same shape and height as the Nordvik Freeze tub with a matching lid design.
The 100ml cup will be of the same shape and height of the Nordvik Freeze Single Serve cup with a matching lid design and includes a spoon inside.

We're looking for edgy clean designs that give an impression of quality and draw attention to the product if it sat on a product shelf. Inspired by packaging such as Ko, Pemberly and Harrowfield we're keen on a black themed packaging with a striking contrast of simple colour and a simple ice cream or gelato image that shows more than one flavour.
This particular design is not boasting any particular flavour, its a uniform design across our whole range of flavours.

Our company logo may be too fussy for this packaging so we would like to include our company ice cream logo and a way to include our company name but still look edgy for example - just like Pemberly Tea - our ice cream logo big G underneath, then 'VILLA ROSA DOLCI' underneath, and below that 'ARTISAN ITALIAN GELATO'. Or anything that inspires and looks good, will draw attention and looks sexy and indulgent and gives an impression of luxury product.

Please check attached document for cup shape and dimensions.

Reason: Christmas and New Year Holiday period resulted in less time for feedback opportunity and new designs to be posted.

Target Market(s)

Target market between 20-40 years old, consumers of quality desserts all year round.

Industry/Entity Type

It Company

Requirements
Must have
• Our Ice Cream Logo
Our name (doesn't need to necessarily have it in our font, can be in bold lettering)
Nice to have
• Limited writing and fuss.
Ideal to have simple clean designs
Should not have
• Eccentric colours and fun childlike images.

```html
<!DOCTYPE html>
<html lang="en">
<head>
<meta charset="utf-8">
<title>Villa Rosa Dolci – 500ml Gelato Tub</title>
<link rel="stylesheet" href="https://fonts.googleapis.com/css2?family=Montserrat:wght@300;400&display=swap">
<style>
  :root {
    --page: #ffffff;
    --tub-black: #0b0709;
    --glow-plum: #6a1045;
    --glow-deep: #2a0619;
    --accent-pink: #d4136f;
    --ink-white: #f4f1f2;
  }
  html, body {
    margin: 0;
    padding: 0;
    width: 1200px;
    height: 1200px;
    overflow: hidden;
    background: var(--page);
    font-family: "Montserrat", Arial, sans-serif;
  }
  .canvas {
    position: relative;
    width: 1200px;
    height: 1200px;
  }

  /* Lid */
  .lid {
    position: absolute;
    left: 390px;
    top: 30px;
    width: 420px;
    height: 420px;
    border-radius: 50%;
    background: var(--tub-black);
  }
  .lid-ring {
    position: absolute;
    inset: 14px;
    border-radius: 50%;
    border: 2px solid var(--accent-pink);
    overflow: hidden;
  }
  .lid-mark {
    position: absolute;
    top: 58px;
    left: 50%;
    width: 84px;
    height: 84px;
    margin-left: -44px;
    border-radius: 50%;
    border: 2px solid var(--ink-white);
  }
  .lid-name {
    position: absolute;
    top: 158px;
    width: 100%;
    text-align: center;
    color: var(--ink-white);
    font-weight: 300;
    font-size: 32px;
    letter-spacing: 1px;
    line-height: 1.2;
  }
  .lid-volume {
    position: absolute;
    top: 212px;
    width: 100%;
    text-align: center;
    color: var(--ink-white);
    font-weight: 400;
    font-size: 14px;
  }
  .lid-divider {
    position: absolute;
    top: 250px;
    left: 0;
    right: 0;
    height: 1px;
    background: var(--accent-pink);
    opacity: 0.7;
  }
  .lid-tagline {
    position: absolute;
    top: 270px;
    width: 100%;
    text-align: center;
    color: var(--ink-white);
    font-weight: 400;
    font-size: 13px;
    letter-spacing: 1.2px;
  }

  /* Side wrap */
  .side-wrap {
    position: absolute;
    left: 180px;
    top: 480px;
    width: 840px;
    height: 610px;
    background: var(--tub-black);
    overflow: hidden;
  }
  .side-glow {
    position: absolute;
    left: 0;
    right: 0;
    top: 60px;
    height: 445px;
    background: radial-gradient(ellipse 48% 60% at 50% 55%, var(--glow-plum) 0%, var(--glow-deep) 55%, var(--tub-black) 100%);
  }
  .side-glow-edge {
    position: absolute;
    left: 0;
    right: 0;
    top: 505px;
    height: 1px;
    background: var(--accent-pink);
    opacity: 0.8;
  }
  .side-mark {
    position: absolute;
    top: 130px;
    left: 50%;
    width: 160px;
    height: 160px;
    margin-left: -82px;
    border-radius: 50%;
    border: 2px solid var(--ink-white);
  }
  .side-name {
    position: absolute;
    top: 318px;
    width: 100%;
    text-align: center;
    color: var(--ink-white);
    font-weight: 300;
    font-size: 62px;
    letter-spacing: 2px;
    line-height: 1.2;
  }
  .side-volume {
    position: absolute;
    top: 448px;
    width: 100%;
    text-align: center;
    color: var(--ink-white);
    font-weight: 400;
    font-size: 22px;
  }
  .side-tagline {
    position: absolute;
    top: 532px;
    width: 100%;
    text-align: center;
    color: var(--ink-white);
    font-weight: 400;
    font-size: 19px;
    letter-spacing: 1.5px;
  }
</style>
</head>
<body>
<main class="canvas">

  <section class="lid" aria-label="Tub lid">
    <div class="lid-ring">
      <div class="lid-mark" role="img" aria-label="Place for the brand's ice cream logo"></div>
      <div class="lid-name">Villa Rosa Dolci</div>
      <div class="lid-volume">500ml</div>
      <div class="lid-divider"></div>
      <div class="lid-tagline">ARTISAN ITALIAN GELATO</div>
    </div>
  </section>

  <section class="side-wrap" aria-label="Tub side label">
    <div class="side-glow" role="img" aria-label="Soft plum smoke-like glow behind the brand name"></div>
    <div class="side-glow-edge"></div>
    <div class="side-mark" role="img" aria-label="Place for the brand's ice cream logo"></div>
    <div class="side-name">Villa Rosa Dolci</div>
    <div class="side-volume">500ml</div>
    <div class="side-tagline">ARTISAN ITALIAN GELATO</div>
  </section>

</main>
</body>
</html>
```